Welcome Card

We are a property management company and I need to attach this postcard to 2 packages of microwave popcorn as a welcome gift to our new tenant.Here is the copy for the postcard (FRONT SIDE): Just "popped" in to make sure your apartment was ready for you! Enjoy your Stay.........UNITED APARTMENTSBACK SIDE: Welcome image with the words "Thank You"

It Company

Sans Serif

```html
<!DOCTYPE html>
<html lang="en">
<head>
<meta charset="utf-8">
<title>Meridale Apartments – Welcome Card</title>
<link rel="stylesheet" href="https://fonts.googleapis.com/css2?family=Fredoka:wght@500;600;700&family=Crimson+Text&family=Open+Sans:wght@300;400&display=swap">
<style>
  :root {
    --card-grey: #e8e8e8;
    --divider-white: #ffffff;
    --band-steel: #4a7fb0;
    --welcome-blue: #1144fb;
    --ink-charcoal: #3a3a3a;
    --ink-edge: #f4f4f4;
    --pop-red: #e51d3a;
    --pop-rim: #ffffff;
    --pop-halo: #d9b98a;
    --logo-ink: #111111;
    --popcorn-cream: #efe6cf;
    --popcorn-blue: #c9d4f2;
  }
  * { margin: 0; padding: 0; box-sizing: border-box; }
  html, body { width: 1200px; height: 930px; overflow: hidden; background: var(--card-grey); }
  .card { position: relative; width: 1200px; height: 930px; background: var(--card-grey); overflow: hidden; }

  .side-divider { position: absolute; left: 905px; top: 0; width: 7px; height: 705px; background: var(--divider-white); }
  .steel-band { position: absolute; left: 0; top: 705px; width: 1200px; height: 12px; background: var(--band-steel); }
  .welcome-panel { position: absolute; left: 0; top: 717px; width: 905px; height: 213px; background: var(--welcome-blue); color: #fff; }

  .headline-lead {
    position: absolute; left: 70px; top: 70px;
    font: 700 94px/1 "Fredoka", sans-serif;
    color: var(--ink-charcoal);
    -webkit-text-stroke: 2px #222;
    text-shadow: 2px 2px 0 var(--ink-edge);
    letter-spacing: 1px;
  }
  .headline-pop {
    position: absolute; left: 440px; top: 292px;
    transform: translate(-50%, -50%) rotate(-34deg);
    white-space: nowrap;
    font: 700 108px/1 "Fredoka", sans-serif;
    color: var(--pop-red);
    -webkit-text-stroke: 4px #7a1020;
    paint-order: stroke fill;
    text-shadow: 5px 5px 0 var(--pop-rim), -5px -5px 0 var(--pop-rim), 5px -5px 0 var(--pop-rim), -5px 5px 0 var(--pop-rim), 9px 9px 0 var(--pop-halo), -9px -9px 0 var(--pop-halo), 9px -9px 0 var(--pop-halo), -9px 9px 0 var(--pop-halo);
  }
  .message {
    position: absolute; left: 370px; top: 328px; width: 540px;
    text-align: center;
    font: 700 45px/90px "Fredoka", sans-serif;
    color: var(--ink-charcoal);
    -webkit-text-stroke: 1px #222;
  }
  .message .signoff { display: block; font-size: 42px; letter-spacing: 0.5px; }

  .brand-name {
    position: absolute; left: 930px; top: 120px; width: 245px;
    text-align: center;
    font: 600 34px/1.15 "Fredoka", sans-serif;
    color: var(--logo-ink);
  }
  .popcorn-photo {
    position: absolute; left: 912px; top: 250px; width: 288px; height: 440px;
    background: radial-gradient(ellipse at 50% 60%, var(--popcorn-blue) 0%, var(--popcorn-cream) 45%, var(--card-grey) 80%);
  }

  .welcome-title { position: absolute; left: 70px; top: 22px; font: 400 45px/1 "Crimson Text", serif; }
  .welcome-copy { position: absolute; left: 112px; top: 92px; font: 300 12.9px/22px "Open Sans", sans-serif; text-transform: uppercase; }
</style>
</head>
<body>
<main class="card">
  <div class="side-divider"></div>

  <h1 class="headline-lead">We Just</h1>
  <div class="headline-pop">POPPED</div>
  <p class="message">
    in to make sure your<br>
    apartment was ready for<br>
    you! Enjoy your Stay
    <span class="signoff">MERIDALE APARTMENTS</span>
  </p>

  <div class="brand-name">MERIDALE<br>apartments</div>
  <div class="popcorn-photo" role="img" aria-label="Photo of a striped popcorn box overflowing with popcorn"></div>

  <div class="steel-band"></div>
  <section class="welcome-panel">
    <h2 class="welcome-title">Welcome Home</h2>
    <p class="welcome-copy">
      Small paragraph small paragraph small paragraph small paragraph small paragraph<br>
      Small paragraph small paragraph small paragraph small paragraph small paragraph
    </p>
  </section>
</main>
</body>
</html>
```